Flyer Design Project for a Seminar "Crossing The Bridge Ahead"

QTVM Chartered Accountants would like a flyer invitation designed for our upcoming seminar "Crossing The Bridge Ahead." The invitation should be created in MS Word, for editing capabilities on our end.

Seminar Title: "Crossing The Bridge Ahead: Securing and Growing Worth Through An Ownership Shift"

This is a complimentary breakfast seminar for Owners and CEOs of private corporations with revenues ranging from $2M to $150M.

Please leave substantial room to enter overview information on the seminar and topics of discussion.

We are open to bold colours and interesting graphics.

An example of a very amateur in-house design is attached.

Target Market(s)

Business owners and CEOs (typically men between 40 and 50 years old)

Industry/Entity Type

Business

Requirements
Must have
• -Substantial space to enter overview info about the seminar
-Space to enter logistical info about the seminar (i.e When, Where and RSVP info)
-Text should be Gill Sans. 1 page only
Should not have
• Stock photos of fake office people or American dollars (we are a Canadian company)!

```html
<!DOCTYPE html>
<html lang="en">
<head>
<meta charset="utf-8">
<title>Crossing The Bridge Ahead – Breakfast Seminar Flyer</title>
<link href="https://fonts.googleapis.com/css2?family=Lato:wght@400;700;900&family=Roboto+Condensed:wght@700&display=swap" rel="stylesheet">
<style>
  :root {
    --backdrop: #e9e6e1;
    --paper: #ffffff;
    --navy: #1d3f78;
    --navy-deep: #16305e;
    --title-blue: #1f4f96;
    --panel-top: #1d3c72;
    --panel-bottom: #4b86cc;
    --tab-blue: #3c73bb;
    --yellow: #f7c51a;
    --orange: #f29a17;
    --ink: #2a2a2a;
    --bullet: #1a2fc0;
    --white: #ffffff;
  }
  * { box-sizing: border-box; margin: 0; padding: 0; }
  html, body { width: 1200px; height: 900px; overflow: hidden; }
  body { background: var(--backdrop); font-family: "Lato", "Gill Sans", sans-serif; color: var(--ink); }

  .flyer {
    position: absolute; left: 40px; top: 50px; width: 1120px; height: 800px;
    background: var(--paper); overflow: hidden;
  }

  /* Header */
  .masthead { position: absolute; left: 0; top: 0; width: 1120px; height: 205px; background: var(--paper); }
  .masthead-swoosh { position: absolute; left: 0; top: 0; }
  .masthead-rule { position: absolute; left: 0; top: 205px; width: 1120px; height: 7px; background: var(--navy-deep); }
  .event-title {
    position: absolute; left: 225px; top: 30px;
    font-family: "Roboto Condensed", "Arial Narrow", sans-serif; font-weight: 700;
    font-size: 38px; letter-spacing: -0.5px; color: var(--title-blue); line-height: 1;
  }
  .event-title-reflection {
    position: absolute; left: 225px; top: 68px;
    font-family: "Roboto Condensed", "Arial Narrow", sans-serif; font-weight: 700;
    font-size: 38px; letter-spacing: -0.5px; line-height: 1; color: var(--title-blue);
    transform: scaleY(-1); opacity: 0.16; height: 22px; overflow: hidden;
  }
  .event-subtitle {
    position: absolute; left: 45px; top: 96px;
    font-weight: 700; font-size: 17px; line-height: 1.2; letter-spacing: 0.8px; color: var(--title-blue);
  }
  .event-audience {
    position: absolute; left: 45px; top: 148px; width: 470px;
    font-size: 14.5px; line-height: 1.25; color: var(--ink);
  }
  .event-date {
    position: absolute; left: 540px; top: 104px; width: 200px; text-align: center;
    font-weight: 700; color: var(--title-blue); line-height: 1.3;
  }
  .event-date .day { font-size: 20px; display: block; }
  .event-date .date { font-size: 15px; display: block; }
  .community-art {
    position: absolute; left: 790px; top: 22px; width: 310px; height: 170px;
    background: radial-gradient(ellipse at 50% 55%, #ffffff 0%, #dfe7f2 45%, #9fb4d3 100%);
    border-radius: 50%;
  }

  /* Body */
  .backdrop-art { position: absolute; left: 0; top: 212px; }

  .side-tab {
    position: absolute; left: -20px; width: 125px; height: 88px;
    background: linear-gradient(180deg, #5d92d6, var(--tab-blue));
    border-radius: 14px; box-shadow: 2px 3px 5px rgba(0,0,0,0.25);
  }
  .side-tab.upper { top: 278px; }
  .side-tab.lower { top: 550px; }

  .overview { position: absolute; left: 115px; top: 283px; width: 550px; font-size: 14.5px; line-height: 1.42; }
  .overview .lead { font-size: 16px; line-height: 1.4; margin-bottom: 12px; }
  .overview p { margin-bottom: 12px; }
  .overview h2 { font-size: 15.5px; font-weight: 700; color: var(--navy-deep); margin: 8px 0 6px 8px; }
  .topics { list-style: none; margin: 0 0 14px 32px; }
  .topics li { position: relative; padding-left: 22px; margin-bottom: 3px; }
  .topics li::before {
    content: ""; position: absolute; left: 0; top: 6px; width: 9px; height: 9px; background: var(--bullet);
  }

  .sponsors { position: absolute; left: 55px; top: 718px; display: flex; gap: 14px; }
  .sponsor-name {
    background: var(--white); padding: 10px 14px; height: 50px;
    display: flex; align-items: center;
    font-weight: 700; font-size: 17px; letter-spacing: 1px; color: var(--navy-deep);
  }

  /* Logistics panel */
  .logistics {
    position: absolute; left: 705px; top: 240px; width: 440px; height: 515px;
    background: linear-gradient(180deg, var(--panel-top) 0%, var(--panel-bottom) 100%);
    border-radius: 48px 0 0 48px;
  }
  .logistics-frame {
    position: absolute; left: 10px; top: 8px; right: -20px; bottom: 8px;
    border: 2px dashed rgba(255,255,255,0.85); border-right: none; border-radius: 42px 0 0 42px;
  }
  .logistics-copy { position: absolute; left: 30px; top: 38px; width: 360px; color: var(--white); font-size: 15.5px; line-height: 1.35; }
  .logistics-copy h3 { font-size: 16px; font-weight: 700; margin-bottom: 12px; }
  .logistics-copy .block { margin-bottom: 32px; }
  .logistics-copy a { color: var(--white); }
  .logistics-note { font-size: 12.5px; line-height: 1.45; opacity: 0.85; }
</style>
</head>
<body>
  <main class="flyer">
    <header class="masthead">
      <svg class="masthead-swoosh" width="1120" height="40" viewBox="0 0 1120 40" aria-hidden="true">
        <path d="M0 0 L1120 0 L1120 22 C800 2 400 30 0 12 Z" fill="#f7c51a"/>
        <path d="M0 0 L1120 0 L1120 10 C800 -2 400 18 0 5 Z" fill="#f29a17"/>
      </svg>
      <h1 class="event-title">Crossing The Bridge Ahead:</h1>
      <div class="event-title-reflection" aria-hidden="true">Crossing The Bridge Ahead:</div>
      <p class="event-subtitle">Protecting, Maximizing &amp; Realizing Value<br>in Today’s Economic Environment</p>
      <p class="event-audience">A complimentary breakfast seminar for Owners and CEOs of private corporations with revenues ranging from $2 Million to $150 Million</p>
      <p class="event-date"><span class="day">Thursday,</span><span class="date">February 24, 2011</span><span class="date">7:45 – 10:00 AM</span></p>
      <div class="community-art" role="img" aria-label="Illustration of a ring of business people holding hands"></div>
    </header>
    <div class="masthead-rule"></div>

    <svg class="backdrop-art" width="1120" height="588" viewBox="0 0 1120 588" aria-hidden="true">
      <defs>
        <linearGradient id="field" x1="0" y1="0" x2="1" y2="1">
          <stop offset="0" stop-color="#f4a51a"/>
          <stop offset="0.35" stop-color="#fbd52c"/>
          <stop offset="0.7" stop-color="#f9c51e"/>
          <stop offset="1" stop-color="#f29a17"/>
        </linearGradient>
        <linearGradient id="sweep" x1="0" y1="0" x2="1" y2="0">
          <stop offset="0" stop-color="#fde66a"/>
          <stop offset="1" stop-color="#f7c51a"/>
        </linearGradient>
      </defs>
      <rect width="1120" height="588" fill="url(#field)"/>
      <path d="M0 40 C300 10 600 90 1120 30 L1120 0 L0 0 Z" fill="#e98c14" opacity="0.5"/>
      <path d="M0 430 C250 380 520 470 1120 420 L1120 588 L0 588 Z" fill="url(#sweep)" opacity="0.7"/>
      <path d="M0 510 C300 470 600 560 1120 500 L1120 520 C600 580 300 500 0 530 Z" fill="#ffffff" opacity="0.55"/>
      <path d="M0 540 C320 500 640 590 1120 540 L1120 588 L0 588 Z" fill="#f08a15"/>
      <path d="M0 565 C350 540 700 600 1120 570 L1120 588 L0 588 Z" fill="#e57a12"/>
    </svg>

    <div class="side-tab upper"></div>
    <div class="side-tab lower"></div>

    <section class="overview">
      <p class="lead">Almost <strong>two-thirds of independent business owners</strong> in Canada are planning to exit their business within the next decade. The spoils will go to those who have planned in advance. Are you one of them?</p>
      <p>Join Martin Hale, Partner at QTVM Chartered Accountants, and Owen Lisowski, Co-Founder of Larkvane Quillory Partners, for a compelling overview of one of the most critical issues affecting privately-held businesses today.</p>
      <h2>Topics of discussion will include:</h2>
      <ul class="topics">
        <li>The alternatives for exiting a business and the implications of each</li>
        <li>Tax minimization strategies for the sale/transfer of your business</li>
        <li>Tactics for gaining control of the deal to achieve a successful sale and maximize the value you receive from it</li>
        <li>Real-life case studies and lessons to be learned from them</li>
      </ul>
      <p>All attendees will receive detailed seminar handouts and a complimentary consultation with both Martin and Owen to map out the next steps in developing an effective exit plan for their business.</p>
    </section>

    <div class="sponsors">
      <span class="sponsor-name">QTVM</span>
      <span class="sponsor-name">LARKVANE QUILLORY</span>
    </div>

    <aside class="logistics">
      <div class="logistics-frame"></div>
      <div class="logistics-copy">
        <div class="block">
          <h3>When:</h3>
          <p>Thursday, February 24, 2011<br>7:45 – 10:00 AM</p>
        </div>
        <div class="block">
          <h3>Where:</h3>
          <p>QTVM Chartered Accountants<br>1870 Bayview Avenue, Suite 300<br>Toronto</p>
        </div>
        <div class="block">
          <h3>RSVP:</h3>
          <p>Contact Claire Dubois at<br>416.555.0198 x 142<br>&nbsp;or <a href="mailto:seminars@qtvm.ca">seminars@qtvm.ca</a></p>
        </div>
        <p class="logistics-note">Pre-registration is required!<br>Seats are limited and will be reserved<br>&nbsp;on a first-come, first-served basis.</p>
      </div>
    </aside>
  </main>
</body>
</html>
```